Disability Service Provider needs a flyer

Project Description:
We are seeking a creative and engaging flyer design to promote a twelve week independent living skills program, focusing on key areas such as money management, basic cooking, food safety, and personal well-being and interpersonal skills. The flyer will be used to encourage individuals to enhance their abilities to live independently and confidently.

Target Audience:
Our target audience includes young adults with a disability and individuals transitioning into independent living situations. We aim to reach those who may be new to managing their own finances, cooking for themselves, and maintaining a healthy lifestyle.

Key Messages:

Independent Living Skills: Emphasize the importance of acquiring essential skills for independent living.
Money Management: Highlight budgeting tips, saving strategies, and financial planning.
Basic Cooking: Showcase simple recipes, cooking techniques, and meal preparation tips.
Food Safety: Provide information on safe food handling practices, storage guidelines, and hygiene.
Personal Well-being: Promote self-care practices, stress management techniques, and mental health awareness.

Target Market(s)

Young adults looking to live independently on their own or with friends

Industry/Entity Type

community services sector

Colors
0054AA
0677BA
7BADD7
CADEEF
E8F1F8

Requirements
Must have
• refer to brief

```html
<!DOCTYPE html>
<html lang="en">
<head>
<meta charset="UTF-8">
<title>Independent Living Skills Flyer</title>
<link href="https://fonts.googleapis.com/css2?family=Poppins:wght@400;500;600;700;800&display=swap" rel="stylesheet">
<style>
  :root {
    --page-bg: #f3ecee;
    --flyer-dark: #1c2321;
    --flyer-mid: #3a4541;
    --accent: #35d37a;
    --accent-deep: #1fa95b;
    --text-light: #ffffff;
    --text-soft: #dfe6e2;
  }
  * { box-sizing: border-box; margin: 0; padding: 0; }
  html, body {
    width: 1200px; height: 962px; overflow: hidden;
    background: var(--page-bg);
    font-family: "Poppins", sans-serif;
  }
  .stage {
    width: 1200px; height: 962px;
    display: flex; align-items: center; justify-content: center;
  }
  .flyer {
    position: relative;
    width: 600px; height: 849px;
    overflow: hidden;
    background: var(--flyer-dark);
    box-shadow: 0 20px 40px rgba(60, 30, 40, 0.18);
  }
  .photo {
    position: absolute; inset: 0;
    background:
      radial-gradient(ellipse 48% 55% at 70% 60%, #2f9b56 0%, rgba(47,155,86,0.35) 45%, transparent 75%),
      linear-gradient(180deg, #2a3230 0%, #4a5552 45%, #3d4643 70%, #2b322f 100%);
  }
  .shade {
    position: absolute; inset: 0;
    background: linear-gradient(90deg, rgba(20,26,24,0.85) 0%, rgba(20,26,24,0.55) 45%, rgba(20,26,24,0.05) 75%),
                linear-gradient(180deg, rgba(20,26,24,0.85) 0%, rgba(20,26,24,0.2) 30%, transparent 60%);
  }
  .content { position: absolute; inset: 0; padding: 44px 40px; color: var(--text-light); }
  .title { font-weight: 800; font-size: 60px; line-height: 1.0; letter-spacing: -0.5px; }
  .title .line-accent { color: var(--accent); display: block; }
  .intro { margin-top: 16px; font-size: 15px; line-height: 1.35; max-width: 330px; color: var(--text-soft); }
  .skills { list-style: none; margin-top: 26px; display: flex; flex-direction: column; gap: 20px; }
  .skill { display: flex; align-items: flex-start; gap: 14px; }
  .skill-icon {
    flex: none; width: 54px; height: 54px; border-radius: 12px;
    background: var(--accent);
    display: flex; align-items: center; justify-content: center;
  }
  .skill-name { font-size: 16px; font-weight: 700; margin-top: 4px; }
  .skill-text { font-size: 11px; line-height: 1.35; color: var(--text-soft); max-width: 250px; }
  .when { margin-top: 30px; }
  .when-on { font-size: 17px; font-weight: 600; }
  .when-date { font-size: 56px; font-weight: 800; color: var(--accent); line-height: 1.05; }
  .when-date sup { font-size: 26px; vertical-align: 26px; }
  .details { list-style: none; margin-top: 14px; display: flex; flex-direction: column; gap: 6px; font-size: 14px; font-weight: 600; }
  .details li { display: flex; align-items: center; gap: 8px; }
  .bands { position: absolute; left: 0; bottom: 0; width: 600px; height: 260px; }
</style>
</head>
<body>
<main class="stage">
  <article class="flyer">
    <div class="photo" role="img" aria-label="Photo of a smiling man in a green jacket and cap walking with crutches outside a building"></div>
    <div class="shade"></div>

    <svg class="bands" viewBox="0 0 600 260" preserveAspectRatio="none" aria-hidden="true">
      <polygon points="0,150 600,40 600,260 0,260" fill="#35d37a" opacity="0.55"/>
      <polygon points="0,200 600,95 600,260 0,260" fill="#1fa95b" opacity="0.6"/>
      <line x1="0" y1="140" x2="600" y2="30" stroke="#ffffff" stroke-width="3"/>
      <line x1="0" y1="162" x2="600" y2="52" stroke="#35d37a" stroke-width="4"/>
    </svg>

    <div class="content">
      <h1 class="title">Independent<span class="line-accent">Living Skills</span></h1>
      <p class="intro">Emphasize the importance of acquiring essential skills for independent living.</p>

      <ul class="skills">
        <li class="skill">
          <span class="skill-icon">
            <svg width="30" height="30" viewBox="0 0 30 30"><text x="15" y="25" text-anchor="middle" font-family="Poppins, sans-serif" font-weight="800" font-size="28" fill="#fff">$</text></svg>
          </span>
          <div><h2 class="skill-name">Money Management</h2><p class="skill-text">Highlight budgeting tips, saving strategies, and financial planning.</p></div>
        </li>
        <li class="skill">
          <span class="skill-icon">
            <svg width="32" height="32" viewBox="0 0 32 32"><path d="M4 26 L26 5 L28 8 L12 24 Z M4 26 L9 27 L12 24 Z" fill="#fff"/></svg>
          </span>
          <div><h2 class="skill-name">Basic Cooking</h2><p class="skill-text">Showcase simple recipes, cooking techniques, and meal preparation tips.</p></div>
        </li>
        <li class="skill">
          <span class="skill-icon">
            <svg width="34" height="34" viewBox="0 0 34 34"><path d="M20 6 Q21 15 29 17 Q21 19 20 28 Q19 19 11 17 Q19 15 20 6Z" fill="#fff"/><path d="M9 4 Q9.5 8 13 8.5 Q9.5 9 9 13 Q8.5 9 5 8.5 Q8.5 8 9 4Z" fill="#fff"/><path d="M8 22 Q8.3 25 11 25.5 Q8.3 26 8 29 Q7.7 26 5 25.5 Q7.7 25 8 22Z" fill="#fff"/></svg>
          </span>
          <div><h2 class="skill-name">Food Safety</h2><p class="skill-text">Provide information on safe food handling practices, storage guidelines, and hygiene.</p></div>
        </li>
        <li class="skill">
          <span class="skill-icon">
            <svg width="30" height="30" viewBox="0 0 30 30"><path d="M11 3 H19 V11 H27 V19 H19 V27 H11 V19 H3 V11 H11 Z" fill="#fff" stroke="#fff" stroke-linejoin="round" stroke-width="2"/></svg>
          </span>
          <div><h2 class="skill-name">Personal Well-being</h2><p class="skill-text">Promote self-care practices, stress management techniques, and mental health awareness.</p></div>
        </li>
      </ul>

      <div class="when">
        <p class="when-on">on</p>
        <p class="when-date">26<sup>th</sup> July</p>
      </div>
      <ul class="details">
        <li><svg width="14" height="14" viewBox="0 0 14 14"><circle cx="7" cy="7" r="6" fill="#fff"/><path d="M7 3.5 V7 L9.5 8.5" stroke="#1c2321" stroke-width="1.5" fill="none"/></svg>8 a.m to 8 p.m</li>
        <li><svg width="14" height="14" viewBox="0 0 14 14"><path d="M7 13 C3 8.5 2 6.5 2 5 A5 5 0 0 1 12 5 C12 6.5 11 8.5 7 13Z" fill="none" stroke="#fff" stroke-width="1.6"/><circle cx="7" cy="5" r="1.6" fill="#fff"/></svg>Address, Street, Post Code Number</li>
      </ul>
    </div>
  </article>
</main>
</body>
</html>
```